Order Management User Interface

I need a new design for our order management screens. They need to be end user friendly and contain the data in an easy to read format. These are online orders. I have attached 3 images from the development solution. For now I just need a new UI and ideally would like it delivered in html so we can easily adapt. The screen has multiple tabs to display the different types of data we store. Ideally the end user needs to see customer focused information first.
I have uploaded an example of a different order view that i like.
Industry/Entity Type
Fashion Retail
Coding
Coded - Design and coding required
Number of Pages Required
1 page

```html
<!DOCTYPE html>
<html lang="en">
<head>
<meta charset="utf-8">
<title>Orders</title>
<link href="https://fonts.googleapis.com/css2?family=Nunito:wght@400;600;700&display=swap" rel="stylesheet">
<style>
:root{
  --page:#edf1f8;
  --frame-a:#3f57b5;
  --frame-b:#8a47c4;
  --panel:#ffffff;
  --soft:#f3f5f9;
  --ink:#2b2f3a;
  --muted:#7d8394;
  --line:#e7eaf0;
  --link:#2f4fa3;
  --primary:#2c4d9e;
  --green:#3bb54a;
  --orange:#f3a23a;
  --red:#e0314b;
  --grey:#9aa0ad;
}
*{box-sizing:border-box;margin:0;padding:0}
html,body{width:1200px;height:720px;overflow:hidden;background:var(--page);font-family:"Nunito",sans-serif;color:var(--ink)}
.frame{position:absolute;left:67px;top:60px;width:1067px;height:600px;border-radius:14px;background:linear-gradient(100deg,var(--frame-a),var(--frame-b))}
.brand-name{position:absolute;left:72px;top:78px;width:38px;text-align:center;color:#fff;font-size:9px;font-weight:700;letter-spacing:.2px}
.nav{position:absolute;left:77px;top:118px;width:28px}
.nav-item{height:27px;display:flex;align-items:center;justify-content:center;margin-bottom:1px;border-radius:6px;opacity:.6}
.nav-item.active{background:rgba(255,255,255,.15);opacity:1}
.nav-item svg{width:12px;height:12px;stroke:#fff;fill:none;stroke-width:1.6}
.app{position:absolute;left:115px;top:71px;width:1008px;height:578px;border-radius:10px;background:var(--soft);overflow:hidden}
.app-title{position:absolute;left:12px;top:12px;font-size:14px;font-weight:600}
.search{position:absolute;left:716px;top:9px;width:247px;height:23px;background:#fff;border-radius:4px;font-size:7.5px;color:var(--muted);padding:0 10px;display:flex;align-items:center;justify-content:space-between}
.search svg{width:9px;height:9px;stroke:#b4b9c4;fill:none;stroke-width:1.5}
.avatar{position:absolute;left:975px;top:10px;width:22px;height:22px;border-radius:50%;background:radial-gradient(circle at 40% 40%,#d7623b,#5a2418)}
.order-tabs{position:absolute;left:11px;top:40px;display:flex;font-size:7.5px;color:var(--muted)}
.order-tab{height:22px;padding:0 8px;display:flex;align-items:center;gap:10px;border-radius:4px 4px 0 0;margin-right:6px}
.order-tab.active{background:#fff;color:var(--ink)}
.order-tab span.x{color:#aab0bd}
.body{position:absolute;left:0;top:62px;width:1008px;height:516px;background:#fff}
.details{position:absolute;left:0;top:0;width:145px;height:516px;padding:10px 12px 0 12px;border-right:4px solid #e3e6ec}
.details-head{display:flex;justify-content:space-between;font-size:7.5px;font-weight:600;margin-bottom:10px}
.state{display:flex;align-items:center;gap:4px;font-weight:400}
.field{border-bottom:1px solid var(--line);height:47px;padding-top:5px}
.field .label{font-size:6px;color:var(--muted)}
.field .value{font-size:7.5px;margin-top:6px}
.field.tall{height:68px}
.field .value.green{color:var(--green)}
.field .value.red{color:var(--red)}
.field a{color:var(--muted);font-size:7px}
.scroll{position:absolute;left:145px;top:0;width:4px;height:187px;background:#c8ccd4;border-radius:2px}
.section-tabs{position:absolute;left:159px;top:13px;height:23px;width:459px;background:var(--soft);border-radius:4px;display:flex;align-items:center;padding:0 4px;font-size:7.5px;color:var(--muted);gap:14px}
.section-tabs .active{background:#fff;color:var(--ink);padding:4px 8px;border-radius:3px}
.actions{position:absolute;right:11px;top:13px;display:flex;align-items:center;gap:8px;font-size:7.5px}
.check{width:10px;height:10px;background:var(--primary);border-radius:2px;display:flex;align-items:center;justify-content:center;margin-right:8px}
.check svg{width:7px;height:7px;stroke:#fff;fill:none;stroke-width:2}
.btn-icon{width:24px;height:23px;border-radius:4px;background:var(--soft);display:flex;align-items:center;justify-content:center}
.btn-icon svg{width:10px;height:10px;stroke:var(--muted);fill:none;stroke-width:1.5}
.btn-save{height:23px;padding:0 10px;border-radius:4px;background:var(--primary);color:#fff;display:flex;align-items:center;gap:5px;font-weight:600}
.btn-save svg{width:8px;height:8px;stroke:#fff;fill:none;stroke-width:1.5}
.table{position:absolute;left:159px;top:53px;width:835px;font-size:7.5px}
.row{display:grid;grid-template-columns:15px 20px 64px 58px 85px 62px 53px 59px 51px 54px 53px 123px 60px 64px 1fr;align-items:start;border-bottom:1px solid var(--line);height:42px;padding-top:16px}
.row.head{height:29px;padding-top:6px;color:var(--muted)}
.row.open{height:136px;padding-top:16px}
.plus{color:var(--muted);font-size:11px;line-height:8px}
.sku{color:var(--link);font-weight:600}
.lbl{color:var(--muted)}
.brand{font-weight:700}
.specs{display:grid;grid-template-columns:58px 85px;row-gap:9px}
.specs .v{color:var(--ink)}
.status{display:flex;align-items:center;gap:5px}
.dot{width:8px;height:8px;border-radius:50%;border:1.5px solid currentColor;display:flex;align-items:center;justify-content:center}
.dot::after{content:"";width:4px;height:4px;border-radius:50%;background:currentColor}
.st-new .dot{color:var(--green)}
.st-pend .dot{color:var(--orange)}
.st-canc .dot{color:var(--grey)}
.chev{display:flex;align-items:center;height:10px}
.chev svg{width:8px;height:8px;stroke:var(--muted);fill:none;stroke-width:1.6}
.tscroll{position:absolute;left:994px;width:3px;height:190px;background:#d3d6dd;border-radius:2px;top:116px}
.pager{position:absolute;right:14px;top:489px;font-size:6.5px;color:var(--muted);display:flex;align-items:center;gap:10px}
.pager svg{width:7px;height:7px;fill:none;stroke-width:1.6}
</style>
</head>
<body>
<div class="frame"></div>
<div class="brand-name">Ordo</div>
<nav class="nav">
  <div class="nav-item active"><svg viewBox="0 0 16 16"><path d="M1 2h2l2 8h8l2-6H4"/><circle cx="6" cy="13" r="1"/><circle cx="12" cy="13" r="1"/></svg></div>
  <div class="nav-item"><svg viewBox="0 0 16 16"><path d="M1 4V1h3M12 1h3v3M15 12v3h-3M4 15H1v-3M5 5v6M8 5v6M11 5v6"/></svg></div>
  <div class="nav-item"><svg viewBox="0 0 16 16"><path d="M8 15s5-5 5-9a5 5 0 0 0-10 0c0 4 5 9 5 9z"/><circle cx="8" cy="6" r="2"/></svg></div>
  <div class="nav-item"><svg viewBox="0 0 16 16"><rect x="2" y="1" width="12" height="14" rx="1"/><circle cx="8" cy="6" r="2"/><path d="M5 12c1-2 5-2 6 0"/></svg></div>
  <div class="nav-item"><svg viewBox="0 0 16 16"><path d="M1 8s3-5 7-5 7 5 7 5-3 5-7 5-7-5-7-5z"/><circle cx="8" cy="8" r="2"/></svg></div>
  <div class="nav-item"><svg viewBox="0 0 16 16"><rect x="3" y="7" width="10" height="8" rx="1"/><path d="M5 7V5a3 3 0 0 1 6 0v2"/></svg></div>
</nav>

<main class="app">
  <h1 class="app-title">Orders</h1>
  <div class="search">Search order... <svg viewBox="0 0 16 16"><circle cx="7" cy="7" r="5"/><path d="M11 11l4 4"/></svg></div>
  <div class="avatar" role="img" aria-label="User profile photo"></div>
  <div class="order-tabs">
    <div class="order-tab active">Order 978393 <span class="x">×</span></div>
    <div class="order-tab">Order 978393 <span class="x">×</span></div>
    <div class="order-tab">Order 978393 <span class="x">×</span></div>
  </div>

  <section class="body">
    <aside class="details">
      <div class="details-head">Details <span class="state st-new"><span class="dot"></span>New</span></div>
      <div class="field"><div class="label">Order No.</div><div class="value">238923892</div></div>
      <div class="field"><div class="label">Original Order No.</div><div class="value">238923892</div></div>
      <div class="field"><div class="label">Customer No.</div><div class="value">#232</div></div>
      <div class="field"><div class="label">Total Retail</div><div class="value green">105.50</div></div>
      <div class="field tall"><div class="label">Instructions</div><div class="value">Lorem ipsum dolor sit amet, consetetu Lorem ipsum...<br><a href="#">Readmore</a></div></div>
      <div class="field"><div class="label">Brand</div><div class="value">238923892</div></div>
      <div class="field"><div class="label">Reference</div><div class="value">238923892</div></div>
      <div class="field"><div class="label">Full Name</div><div class="value">Test Order</div></div>
      <div class="field"><div class="label">Total Tax</div><div class="value red">9.55</div></div>
      <div class="field"><div class="label">Order Type</div><div class="value">Sale</div></div>
    </aside>
    <div class="scroll"></div>

    <div class="section-tabs">
      <span class="active">Items</span><span>Customer(s)</span><span>Addresses</span><span>Payments</span><span>Vouchers</span><span>Event Queues</span><span>Updates</span><span>Fulfilments</span><span>History</span>
    </div>
    <div class="actions">
      Authority to leave <span class="check"><svg viewBox="0 0 10 10"><path d="M2 5l2 2 4-4"/></svg></span>
      <span class="btn-icon"><svg viewBox="0 0 16 16"><path d="M13 6a5 5 0 0 0-9-1M3 10a5 5 0 0 0 9 1M4 2v3h3M12 14v-3H9"/></svg></span>
      <span class="btn-save"><svg viewBox="0 0 16 16"><path d="M2 2h10l2 2v10H2z"/><path d="M5 2v4h6V2M5 14v-4h6v4"/></svg>Save</span>
    </div>

    <div class="table">
      <div class="row head"><span></span><span></span><span>SKU</span><span>Product</span><span></span><span>Is Dropship</span><span>Quantity</span><span>Unit Retail</span><span>Unit Tax</span><span>Discount</span><span>Final Price</span><span>Discount Reason</span><span>Coupon Code</span><span>Status</span><span></span></div>

      <div class="row open"><span></span><span class="plus">+</span><span class="sku">2230566</span>
        <div class="specs" style="grid-column:span 2">
          <span class="lbl">Vendor</span><span class="brand">Orchard Co</span>
          <span class="lbl">Brand</span><span class="v">Orchard</span>
          <span class="lbl">Product Code</span><span class="v">20022569</span>
          <span class="lbl">Description</span><span class="v">PJ SET</span>
          <span class="lbl">Colour (Code)</span><span class="v">900</span>
          <span class="lbl">Size</span><span class="v">12/14</span>
        </div>
        <span>Yes</span><span>23</span><span>35.00</span><span>3.18</span><span>0.00</span><span>35.00</span><span>50% discount for early birds</span><span>324ASD</span><span class="status st-new"><span class="dot"></span>New</span><span class="chev"><svg viewBox="0 0 10 10"><path d="M2 7l3-3 3 3"/></svg></span></div>

      <div class="row"><span></span><span class="plus">+</span><span class="sku">2323232</span><span class="lbl">Vendor</span><span class="brand">Norvale</span><span>Yes</span><span>3</span><span>35.00</span><span>3.18</span><span>0.00</span><span>35.00</span><span>50% discount for early birds</span><span>324ASD</span><span class="status st-new"><span class="dot"></span>New</span><span class="chev"><svg viewBox="0 0 10 10"><path d="M2 3l3 3 3-3"/></svg></span></div>
      <div class="row"><span></span><span class="plus">+</span><span class="sku">4545454</span><span class="lbl">Vendor</span><span class="brand">Kestrel</span><span>No</span><span>23</span><span>35.00</span><span>3.18</span><span>0.00</span><span>35.00</span><span>-</span><span>324ASD</span><span class="status st-pend"><span class="dot"></span>Pending</span><span class="chev"><svg viewBox="0 0 10 10"><path d="M2 3l3 3 3-3"/></svg></span></div>
      <div class="row"><span></span><span class="plus">+</span><span class="sku">2230566</span><span class="lbl">Vendor</span><span class="brand">Lumio</span><span>Yes</span><span>5</span><span>35.00</span><span>3.18</span><span>0.00</span><span>35.00</span><span>-</span><span>324ASD</span><span class="status st-pend"><span class="dot"></span>Pending</span><span class="chev"><svg viewBox="0 0 10 10"><path d="M2 3l3 3 3-3"/></svg></span></div>
      <div class="row"><span></span><span class="plus">+</span><span class="sku">6786788</span><span class="lbl">Vendor</span><span class="brand">Veyra</span><span>No</span><span>23</span><span>35.00</span><span>3.18</span><span>0.00</span><span>35.00</span><span>50% discount for early birds</span><span>324ASD</span><span class="status st-new"><span class="dot"></span>New</span><span class="chev"><svg viewBox="0 0 10 10"><path d="M2 3l3 3 3-3"/></svg></span></div>
      <div class="row"><span></span><span class="plus">+</span><span class="sku">1282122</span><span class="lbl">Vendor</span><span class="brand">Tanzo</span><span>Yes</span><span>23</span><span>35.00</span><span>3.18</span><span>0.00</span><span>35.00</span><span>-</span><span>324ASD</span><span class="status st-canc"><span class="dot"></span>Cancelled</span><span class="chev"><svg viewBox="0 0 10 10"><path d="M2 3l3 3 3-3"/></svg></span></div>
      <div class="row"><span></span><span class="plus">+</span><span class="sku">2321329</span><span class="lbl">Vendor</span><span class="brand">Voltan</span><span>Yes</span><span>23</span><span>35.00</span><span>3.18</span><span>0.00</span><span>35.00</span><span>50% discount for early birds</span><span>324ASD</span><span class="status st-new"><span class="dot"></span>New</span><span class="chev"><svg viewBox="0 0 10 10"><path d="M2 3l3 3 3-3"/></svg></span></div>
    </div>
    <div class="tscroll"></div>

    <div class="pager">1-10 /100
      <svg viewBox="0 0 10 10" stroke="#b4b9c4"><path d="M6 2L3 5l3 3"/></svg>
      <svg viewBox="0 0 10 10" stroke="#2b2f3a"><path d="M4 2l3 3-3 3"/></svg>
    </div>
  </section>
</main>
</body>
</html>
```